Business card design needed

We need a business card design for a new micro business based in Melbourne (Australia). Our main service is cleaning and fixing Vertical Blinds as a cheaper alternative than buying new blinds. A smaller part of the business is fitting affordable & temporary alternatives to double glazed windows both for noise abatement and climate control and reduction in energy costs.
We could be dealing with commercial as well as residential customers so we need a quality look. The design needs to reflect our core business of vertical blinds cleaning & maintenance.

Target Market(s)

Not sure yet. These Business Cards are going to be used to test the market

Industry/Entity Type

Residential

Contact Information for Business Card

Teloria Brinkhaus. Vertical Blinds Cleaning, Maintenance & Temporary Window Insulation Solutions. Ph: 03 9274 5163. Mob: 0497 362 514.

```html
<!DOCTYPE html>
<html lang="en">
<head>
<meta charset="utf-8">
<title>Business Card – Teloria Brinkhaus</title>
<link rel="stylesheet" href="https://fonts.googleapis.com/css2?family=Source+Sans+3:wght@400;700&display=swap">
<style>
  :root {
    --card-grey: #858686;
    --lime: #a8cd3a;
    --white: #ffffff;
    --ink: #231f20;
  }
  html, body {
    margin: 0;
    padding: 0;
    width: 1200px;
    height: 693px;
    overflow: hidden;
    background: var(--card-grey);
  }
  .card {
    position: relative;
    width: 1200px;
    height: 693px;
    background: var(--card-grey);
    font-family: "Source Sans 3", "Myriad Pro", Arial, sans-serif;
    overflow: hidden;
  }
  .service-tile {
    position: absolute;
    top: 111px;
    width: 120px;
    height: 108px;
    border-radius: 14px;
    background: var(--lime);
  }
  .tile-clean { left: 88px; }
  .tile-repair { left: 227px; }
  .tile-inspect { left: 363px; }

  .band {
    position: absolute;
    top: 230px;
    left: 0;
    width: 1200px;
    height: 231px;
    background: var(--white);
  }
  .band-slats {
    position: absolute;
    top: 0;
    height: 100%;
    background: var(--lime);
  }
  .slats-left { left: 0; width: 486px; }
  .slats-right { left: 939px; width: 261px; }

  .contact {
    position: absolute;
    left: 503px;
    top: 230px;
    color: var(--ink);
  }
  .contact-name {
    position: absolute;
    top: 60px;
    left: 0;
    margin: 0;
    font-size: 54px;
    font-weight: 700;
    white-space: nowrap;
    line-height: 1;
  }
  .contact-line {
    position: absolute;
    left: 2px;
    margin: 0;
    font-size: 38px;
    font-weight: 400;
    white-space: nowrap;
    line-height: 1;
  }
  .contact-phone { top: 123px; }
  .contact-mobile { top: 165px; }

  .service {
    position: absolute;
    left: 502px;
    white-space: nowrap;
  }
  .service-title {
    position: absolute;
    left: 0;
    color: var(--lime);
    font-weight: 700;
    font-size: 40px;
    line-height: 1;
  }
  .service-detail {
    position: absolute;
    background: var(--white);
    color: var(--ink);
    font-size: 33px;
    line-height: 1;
    padding-left: 7px;
    box-sizing: border-box;
    display: flex;
    align-items: center;
  }
  .service-blinds { top: 484px; }
  .service-blinds .service-title { top: 0; }
  .service-blinds .service-detail { left: 263px; width: 429px; height: 39px; top: 0; }
  .service-insulation { top: 543px; }
  .service-insulation .service-title { top: 0; }
  .service-insulation .service-detail { left: 355px; width: 337px; height: 40px; top: 0; }
</style>
</head>
<body>
<div class="card">
  <div class="service-tile tile-clean" role="img" aria-label="Cleaning service icon: spray bottle"></div>
  <div class="service-tile tile-repair" role="img" aria-label="Repair service icon: wrench"></div>
  <div class="service-tile tile-inspect" role="img" aria-label="Inspection service icon: magnifying glass"></div>

  <div class="band">
    <div class="band-slats slats-left" role="img" aria-label="Lime and white vertical blind slat pattern"></div>
    <div class="band-slats slats-right" role="img" aria-label="Lime and white vertical blind slat pattern"></div>
  </div>

  <div class="contact">
    <h1 class="contact-name">Teloria Brinkhaus</h1>
    <p class="contact-line contact-phone">Ph: 03 9274 5163</p>
    <p class="contact-line contact-mobile">Mob: 0497 362 514</p>
  </div>

  <div class="service service-blinds">
    <span class="service-title">Vertical Blinds</span>
    <span class="service-detail">Cleaning and Maintenance</span>
  </div>
  <div class="service service-insulation">
    <span class="service-title">Window Temporary</span>
    <span class="service-detail">Insulation Solutions</span>
  </div>
</div>
</body>
</html>
```